Need Brochure Design For Pizza Restaurant

Need redesign for pizza restaurant. Brochure size is 11 Inches X 17 Inches Roll Fold.

Specifications and original menu will be attached.

Target Market(s)

Those who enjoy Pizza ;)

Industry/Entity Type

Restaurant

Requirements
Must have
• The brochure must be double sided.

Must include important information such as operating hours, telephone number, etc.

The brochure should have a snapshot of a map such as Rovi Charts showing the location of the establishment.

All these information could be found on our Rovi Spots page:
http://charts.rovimapex.ca/charts?hl=en&sugexp=frgbld&gs_nf=1&pq=tz+pizza&cp=9&gs_id=4&xhr=t&q=tz%20pizza%20fort%20mcmurray&bav=on.2,or.r_gc.r_pw.r_qf.,cf.osb&biw=1584&bih=810&um=1&ie=UTF-8&sa=N&tab=il

There should be a place where the receiver can cut out a piece of the menu to get a coupon, like in the original design I attached, in which case, there should not be anything important on the reverse side of the brochure where the cut out is to be made.

Final copy needs to be in PDF and PSD, the latter must be separated into layers for ease of later editing.
Nice to have
• Highlight the importance that the establishment is under new management and recently renovated.

```html
<!DOCTYPE html>
<html lang="en">
<head>
<meta charset="UTF-8">
<title>TZ's Pizza Menu</title>
<link rel="stylesheet" href="https://fonts.googleapis.com/css2?family=Alfa+Slab+One&family=Roboto+Condensed:ital,wght@0,400;0,700;1,700&display=swap">
<style>
:root{
  --red:#e2231a;
  --ink:#111;
  --pink:#f7c9c6;
  --pink-soft:#fde9e7;
  --paper:#ffffff;
  --rule:#222;
}
*{box-sizing:border-box;margin:0;padding:0}
html,body{width:1200px;height:776px;overflow:hidden;background:var(--paper)}
body{font-family:"Roboto Condensed",Arial,sans-serif;color:var(--ink);position:relative}
.abs{position:absolute}
.slab{font-family:"Alfa Slab One",Georgia,serif;font-weight:400}

/* left panel */
.wings-photo{left:0;top:0;width:405px;height:290px;background:linear-gradient(100deg,#3f8d2a 0%,#6fb43c 28%,#a35a22 55%,#6b2f12 80%,#3d1a0a 100%)}
.wings-bubble{left:112px;top:22px;width:160px;height:88px;border-radius:50%;background:var(--paper);text-align:center;padding-top:16px;box-shadow:0 2px 4px rgba(0,0,0,.35)}
.wings-bubble .count{font-weight:700;font-size:10px;letter-spacing:1.5px}
.wings-bubble .count b{color:var(--red)}
.wings-bubble .name{font-weight:700;font-size:8.5px}
.wings-bubble p{font-size:7.6px;line-height:1.15;padding:0 10px}
.wings-feature{left:230px;top:196px;width:150px;text-align:center;color:#fff;font-size:13px;line-height:1.1;letter-spacing:.5px}
.wings-feature .price{font-size:17px;margin-top:4px}
.excited{left:46px;top:232px;font-weight:700;font-style:italic;font-size:14px;line-height:1.25;color:var(--ink)}
.excited .hot{color:var(--red)}
.panel-title{color:var(--red);font-size:14px;letter-spacing:.5px}
.apps-title{left:124px;top:292px}
.app-col{width:170px;font-size:6.4px;line-height:1.12}
.app-col.one{left:22px;top:322px}
.app-col.two{left:215px;top:322px}
.app{margin-bottom:2.4px}
.app h4{display:flex;justify-content:space-between;font-size:9px;line-height:1.05;font-weight:700}
.coupon{left:214px;top:558px;width:172px;height:212px;border-left:3px dotted #777;border-right:3px dotted #777}
.coupon-half{height:106px;position:relative;border-top:3px dotted #777}
.coupon-half:last-child{border-bottom:3px dotted #777}
.coupon .line{position:absolute;left:14px;font-size:12px;letter-spacing:1px}
.coupon .buy{top:6px}
.coupon .get{bottom:6px}
.r{color:var(--red)}

/* middle panel */
.pizza-title{left:540px;top:22px}
.garlic-photo{left:505px;top:18px;width:36px;height:42px;border-radius:45% 45% 40% 40%;background:radial-gradient(circle at 40% 40%,#fbf8ee,#d9d0b3)}
.tomato-photo{left:680px;top:0;width:110px;height:64px;border-radius:40px;background:radial-gradient(circle at 35% 35%,#ff6a4a,#c9190f 70%)}
.sizes{left:430px;top:73px;width:364px;display:grid;grid-template-columns:1fr 62px 68px 64px;font-weight:700;font-size:10px;text-align:right}
.menu{left:430px;top:88px;width:364px}
.row{display:grid;grid-template-columns:1fr 62px 68px 64px;border-bottom:1px solid var(--rule);font-size:9.6px;line-height:1.22;padding:.5px 0}
.row .n{font-weight:700}
.row .d{grid-column:1/2;font-size:8px;line-height:1.1;font-weight:400}
.row .p{text-align:right;font-weight:700;align-self:end}
.row.thick{border-bottom-width:1.5px}
.note{font-size:8px;padding:2px 0 1px}
.topping{display:grid;grid-template-columns:88px 1fr;font-size:8.6px;line-height:1.15;margin-top:3px}
.topping b{font-size:9.4px}

/* right panel */
.combos-title{left:873px;top:24px}
.combo-col{top:52px;width:172px}
.combo-col.one{left:840px}
.combo-col.two{left:1018px}
.combo{text-align:center;background:linear-gradient(180deg,var(--pink) 0%,var(--pink-soft) 40%,var(--paper) 100%);border-top:1px solid #e8a9a4;padding:4px 0 6px;margin-bottom:5px}
.combo h3{font-size:13px;font-weight:700;line-height:1.3}
.combo p{font-size:10px;line-height:1.55}
.weekly-title{left:877px;top:530px}
.weekly{left:840px;top:558px;width:174px;font-size:8px;line-height:1.1}
.day h4{display:flex;justify-content:space-between;font-size:9.6px;font-weight:700;line-height:1.15}
.day{margin-bottom:2px}
.deal{display:flex;justify-content:space-between;font-weight:700;font-size:9.6px}
.pasta-photo{left:1026px;top:532px;width:174px;height:240px;background:linear-gradient(160deg,#5a3514 0%,#a86a25 40%,#e4b552 65%,#7a4a1b 100%)}
</style>
</head>
<body>

<!-- left panel -->
<div class="abs wings-photo" role="img" aria-label="Photo of glazed chicken wings with fresh herbs and a mushroom"></div>
<div class="abs wings-bubble">
  <div class="count"><b>12</b> WINGS <b>12</b></div>
  <div class="name">Classic chicken wings</div>
  <p>Deep fried to a golden crisp and can be flavored: Teriyaki, BBQ, Hot, Mild, Salt and Pepper, Golden, Honey Garlic, Thai Chili or Lemon Pepper.</p>
</div>
<div class="abs wings-feature slab">TZ's<br>Chicken<br>Wings<div class="price">$9.95</div></div>
<div class="abs excited">We are so excited!<br>New ownership,<br><span class="hot">Excellent menu!</span></div>

<h2 class="abs panel-title slab apps-title">Appetizers</h2>
<div class="abs app-col one">
  <div class="app"><h4><span>Chubby Chicken Wings</span><span>$11.95</span></h4>They are the biggest, juiciest, and meatiest dozen wings you have ever seen. They can be flavored: Teriyaki, BBQ, Hot, Mild, Salt &amp; Pepper, Golden, Honey Garlic, Thai Chili or Lemon Pepper.</div>
  <div class="app"><h4><span>TZ's Platter</span><span>$14.95</span></h4>Four golden chicken wings, two chicken fingers, two mozza sticks, two jalapeno poppers, two mini beef tacos, two torpedo shrimps and sweet potato fries served with celery sticks, carrot sticks, ranch dressing, plum sauce and salsa.</div>
  <div class="app"><h4><span>Sweet Potato Wedges</span><span>$6.95</span></h4>8 oz. of deep fried sweet potato fries. This delicious snack is an instant TZ's Classic.</div>
  <div class="app"><h4><span>Nachos</span><span>$11.95</span></h4>Nacho chips topped with cheese, green onions, jalapeno peppers, and tomatoes. Served with sour cream and salsa. Add chicken or beef for $3.50.</div>
  <div class="app"><h4><span>Boneless Garlic Ribs</span><span>$8.95</span></h4>8 oz. of garlic ribs sprinkled with Montreal Steak Seasoning and served with plum sauce.</div>
  <div class="app"><h4><span>Jalapeno Poppers</span><span>$8.95</span></h4>Six Jalapenos stuffed with cheese and served with salsa for dipping.</div>
  <div class="app"><h4><span>Quesadilla</span><span>$8.95</span></h4>Sautéed peppers, onions and cheese wrapped in a crispy tortilla shell. Served with salsa and sour cream. Add chicken or beef for $3.50.</div>
  <div class="app"><h4><span>Poutine</span><span>$6.95</span></h4>This classic Canadian treat will surely be delicious.</div>
  <div class="app"><h4><span>Newfoundland Fries</span><span>$7.95</span></h4>Like the classic Canadian Poutine but with a dash of seasoned ground beef.</div>
  <div class="app"><h4><span>Mini Beef Tacos</span><span>$8.95</span></h4>Shredded beef and green chili in a crispy corn tortilla. Served with salsa.</div>
  <div class="app"><h4><span>Onion Rings</span><span>$6.95</span></h4>Onion rings coated with batter and fried with a crisp. Served with ranch dressing.</div>
  <div class="app"><h4><span>Potato Skins</span><span>$8.95</span></h4>Half dozen baked potato wedges topped with real bacon bits, green onions and mozzarella cheese. Served with sour cream.</div>
  <div class="app"><h4><span>Mushroom Caps</span><span>$9.95</span></h4>Stuffed with crab meat and cream cheese, topped off with melted mozzarella cheese and served with garlic toast.</div>
</div>
<div class="abs app-col two">
  <div class="app"><h4><span>Popcorn Shrimp</span><span>$8.95</span></h4>8 oz. of breaded shrimp deep-fried until golden and served with cocktail sauce.</div>
  <div class="app"><h4><span>Mozza Sticks</span><span>$8.95</span></h4>Half dozen delicious deep-fried mozzarella sticks coated with cheese and served with ranch dressing.</div>
  <div class="app"><h4><span>Tempura Butterfly Shrimp</span><span>$10.95</span></h4>Jumbo sized shrimp in mouthwatering tempura batter.</div>
  <div class="app"><h4><span>Tempura Coconut Shrimp</span><span>$10.95</span></h4>Jumbo sized shrimp in mouthwatering tempura batter.</div>
  <div class="app"><h4><span>Breaded Calamari Rings</span><span>$9.95</span></h4>Squid rings coated in batter and deep-fried until golden. Served with dressing.</div>
  <div class="app"><h4><span>Vegetable Spring Rolls</span><span>$6.95</span></h4>Six delicious vegetable rolls. Served with plum sauce.</div>
  <div class="app"><h4><span>Thai Chicken Bites</span><span>$8.95</span></h4>8 oz. of crispy chicken tenders tossed in sweet and hot chili sauce.</div>
  <div class="app"><h4><span>TZ's Natural Cut Chips</span><span>$6.95</span></h4>They taste awesome as it is and even better with spicy seasoning. A must try.</div>
  <div class="app"><h4><span>Torpedo Shrimps</span><span>$10.95</span></h4>Deep fried until golden.</div>
</div>
<div class="abs coupon">
  <div class="coupon-half">
    <div class="line slab buy"><span class="r">BUY</span> ONE</div>
    <div class="line slab get">GET <span class="r">ONE</span></div>
  </div>
  <div class="coupon-half">
    <div class="line slab buy"><span class="r">BUY</span> ONE</div>
    <div class="line slab get">GET <span class="r">ONE</span></div>
  </div>
</div>

<!-- middle panel -->
<div class="abs garlic-photo" role="img" aria-label="Photo of a garlic bulb with parsley"></div>
<h2 class="abs panel-title slab pizza-title"><span class="r">Pizza</span> Pie</h2>
<div class="abs tomato-photo" role="img" aria-label="Photo of ripe tomatoes on the vine"></div>
<div class="abs sizes"><span></span><span>10”</span><span>12”</span><span>14”</span></div>
<div class="abs menu">
  <div class="row"><span class="n">Cheese</span><span class="p">$19.95</span><span class="p">$23.95</span><span class="p">$29.95</span></div>
  <div class="row"><span class="n">Pepperoni</span><span class="p">$21.95</span><span class="p">$25.95</span><span class="p">$31.95</span></div>
  <div class="row"><span class="n">Pepperoni &amp; Mushroom</span><span class="p">$22.95</span><span class="p">$26.95</span><span class="p">$32.95</span></div>
  <div class="row"><span class="n">Hawaiian</span><span class="p">$24.95</span><span class="p">$28.95</span><span class="p">$34.95</span></div>
  <div class="row"><span class="n">Double Bacon<br><span class="d">•Bacon and Back Bacon.</span></span><span class="p">$24.95</span><span class="p">$28.95</span><span class="p">$35.95</span></div>
  <div class="row"><span class="n">Canuck<br><span class="d">•Bacon and Back Bacon.</span></span><span class="p">$25.95</span><span class="p">$29.95</span><span class="p">$36.95</span></div>
  <div class="row"><span class="n">All Dressed<br><span class="d">•Pepperoni, Mushroom, Onion &amp; Green Pepper.</span></span><span class="p">$25.95</span><span class="p">$29.95</span><span class="p">$36.95</span></div>
  <div class="row"><span class="n">Meat Lovers<br><span class="d">•Pepperoni, Ground Beef, Ham &amp; Back Bacon.</span></span><span class="p">$26.95</span><span class="p">$30.95</span><span class="p">$37.95</span></div>
  <div class="row"><span class="n">Greek<br><span class="d">•Black Olive, Onions, Green Peppers,<br>&nbsp;Feta &amp; Tomatoes.</span></span><span class="p">$24.95</span><span class="p">$28.95</span><span class="p">$35.95</span></div>
  <div class="row"><span class="n">Vegetarian<br><span class="d">•Black Olives, Onions, Green Peppers,<br>&nbsp;Mushrooms &amp; Tomatoes.</span></span><span class="p">$24.95</span><span class="p">$29.95</span><span class="p">$36.95</span></div>
  <div class="row"><span class="n">Mexican<br><span class="d">•Salsa, Beef, Onion, Green Pepper,<br>&nbsp;Cheddar &amp; Mozzarella</span></span><span class="p">$25.95</span><span class="p">$29.95</span><span class="p">$36.95</span></div>
  <div class="row"><span class="n">Donair<br><span class="d">•Donair, Onion, Tomatoes &amp; Sweet Sauce.</span></span><span class="p">$25.95</span><span class="p">$29.95</span><span class="p">$36.95</span></div>
  <div class="row"><span class="n">Fire Chicken<br><span class="d">•Salsa, Chicken, Onions &amp; Hot Peppers.</span></span><span class="p">$25.95</span><span class="p">$29.95</span><span class="p">$36.95</span></div>
  <div class="row"><span class="n">Classic Italian<br><span class="d">•Cappacolo, Pepperoni, Green Pepper,<br>&nbsp;Salami &amp; Olives.</span></span><span class="p">$25.95</span><span class="p">$29.95</span><span class="p">$36.95</span></div>
  <div class="row"><span class="n">BBQ Chicken<br><span class="d">•BBQ Sauce, Chicken, Green Peppers &amp; Tomato.</span></span><span class="p">$25.95</span><span class="p">$29.95</span><span class="p">$36.95</span></div>
  <div class="row"><span class="n">Cheese Burger<br><span class="d">•Beef, Mushroom, Onions, Bacon, Cheddar &amp; Mozza.</span></span><span class="p">$26.95</span><span class="p">$30.95</span><span class="p">$37.95</span></div>
  <div class="row"><span class="n">TZ's Special<br><span class="d">•Pepperoni, Mushrooms, Ham, Italian Sausage,<br>&nbsp;Green Pepper &amp; Tomatoes.</span></span><span class="p">$28.95</span><span class="p">$32.95</span><span class="p">$39.95</span></div>
  <div class="row"><span class="n">Garlic Cheese Fingers</span><span class="p">$20.95</span><span class="p">$24.95</span><span class="p">$29.95</span></div>
  <div class="row"><span class="n">Create Your Own</span></div>
  <div class="row"><span class="n">•One Topping</span><span class="p">$20.95</span><span class="p">$24.95</span><span class="p">$31.95</span></div>
  <div class="row"><span class="n">•Two Toppings</span><span class="p">$23.95</span><span class="p">$27.95</span><span class="p">$34.95</span></div>
  <div class="row"><span class="n">•Three Toppings</span><span class="p">$24.95</span><span class="p">$28.95</span><span class="p">$35.95</span></div>
  <div class="row"><span class="n">•Four Toppings</span><span class="p">$25.95</span><span class="p">$29.95</span><span class="p">$36.95</span></div>
  <div class="row thick"><span class="n">•Five Toppings</span><span class="p">$26.95</span><span class="p">$30.95</span><span class="p">$37.95</span></div>
  <div class="note">*Cheeses don’t count as toppings.</div>
  <div class="row thick"><span class="n">1 Pizza Only – Up To Four Toppings</span><span class="p">$14.95</span><span class="p">$19.95</span><span class="p">$24.95</span></div>
  <div class="row" style="border:0"><span class="n">Extra toppings</span><span class="p">$2.50</span><span class="p">$3.00</span><span class="p">$3.50</span></div>
  <div class="topping"><b>Meat Toppings -</b><span>Chicken, Pepperoni, Bacon, Back Bacon, Salami, Ham, Ground Beef, Italian Sausage, Cappacolo &amp; Baby Shrimp.</span></div>
  <div class="topping"><b>Vegetable Toppings -</b><span>Onions, Mushrooms, Tomatoes, Green Peppers, Hot Peppers, Jalapeno, Black Olives, Salsa, Pineapple, Cooked Tomatoes, Extra Cheese, Extra Sauce.</span></div>
  <div class="topping"><b>Cheeses -</b><span>Mozzarella, Cheddar, Feta &amp; Parmesan.</span></div>
  <div class="topping"><b>Dipping Sauces -</b><span>Sweet Sauce. <b style="margin-left:42px">$1.50</b></span></div>
</div>

<!-- right panel -->
<h2 class="abs panel-title slab combos-title"><span class="r">Com</span>bos and Spe<span class="r">cials</span></h2>
<div class="abs combo-col one">
  <div class="combo"><h3>Combo 1 - $31.99</h3><p>3 X 10” Pizza (Three Toppings)<br>2L Pop</p></div>
  <div class="combo"><h3>Combo 2 - $36.99</h3><p>3 X 12” Pizza (Three Toppings)<br>2L Pop</p></div>
  <div class="combo"><h3>Combo 3 - $41.99</h3><p>3 X 14” Pizza (3 Toppings)<br>2L Fizzo</p></div>
  <div class="combo"><h3>Combo 4 - $30.99</h3><p>2 X 10” Pizza (Three Toppings)<br>Dozen Wings • 2L Pop</p></div>
  <div class="combo"><h3>Combo 5 - $36.99</h3><p>2 X 12” Pizza (Three Toppings)<br>Dozen Wings • 2L Pop</p></div>
  <div class="combo"><h3>Combo 6 - $30.99</h3><p>12” Pizza (Three Toppings)<br>Boneless Chicken Wings<br>Caesar Salad • 2L Pop</p></div>
  <div class="combo"><h3>Combo 7 - $34.99</h3><p>2 X Baked Pasta (Garlic Toasts)<br>20 Wings • 2L Pop</p></div>
</div>
<div class="abs combo-col two">
  <div class="combo"><h3>Combo 8 - $30.99</h3><p>10” Pizza (Three Toppings)<br>Rack of Ribs with Spaghetti<br>2L Pop</p></div>
  <div class="combo"><h3>Combo 9 - $30.99</h3><p>10” Pizza (Three Toppings)<br>Ribs and Chicken with Spaghetti<br>2L Pop</p></div>
  <div class="combo"><h3>Combo 10 - $27.99</h3><p>10” Pizza (Three Toppings)<br>Half BBQ Chicken with Spaghetti<br>2L Pop</p></div>
  <div class="combo"><h3>Combo 11 - $36.99</h3><p>12” Pizza (Three Toppings)<br>2 X Baked Pasta • 2L Pop</p></div>
  <div class="combo"><h3>Combo 12 - $31.99</h3><p>10” Pizza (Three Toppings)<br>Baked Pasta<br>Dozen Wings • 2L Pop</p></div>
  <div class="combo"><h3>Combo 13 - $30.99</h3><p>12” Pizza (Three Toppings)<br>2 X Bacon Cheese Burgers<br>Caesar Salad • 2L Pop</p></div>
</div>

<h2 class="abs panel-title slab weekly-title"><span class="r">Weekly</span></h2>
<div class="abs weekly">
  <div class="day"><h4><span>Monday</span><span>$29.95</span></h4>2 For 1 Steak With Garlic Shrimp. Prime Rib, Rib-Eye, New York and T-Bone.</div>
  <div class="day"><h4><span>Tuesday</span><span>$28.95</span></h4>2 For 1 Baby Back Ribs.</div>
  <div class="day"><h4><span>Wednesday</span><span>$16.95</span></h4>2 For 1 Pasta.</div>
  <div class="day"><h4><span>Thursday</span><span>$15.95</span></h4>2 For 1 Chicken or Beef Burgers.</div>
  <div class="day"><h4><span>Friday</span><span>$15.95</span></h4>2 For 1 Fish and Chips.</div>
  <div class="day"><h4><span>Saturday</span><span></span></h4>Kids Under 9 Years Eat FREE With Adult Purchase.</div>
  <div class="day"><h4><span>Sunday</span><span></span></h4>
    <div class="deal"><span>2 For 1 10” 3 Topping Pizza</span><span>$18.95</span></div>
    <div class="deal"><span>2 For 1 12” 3 Topping Pizza</span><span>$23.95</span></div>
  </div>
</div>
<div class="abs pasta-photo" role="img" aria-label="Photo of dry pasta, garlic and olive oil on a rustic table"></div>

</body>
</html>
```